Conference website: Kestrel Meridian Forum 2015

We need a web design to help develop a modern and interactive website for the 2nd Kestrel Meridian Summit which main objective will be to present and discuss real-life KmR business initiatives being implemented by entrepreneurs and corporate innovators that are driving sustainable innovation from the bottom up

This is a bi-annual event and will build on the 1st Kestrel Meridian Forum
http://www.kestrelmeridian.org/summit-2013. It is important that the new website maintain consistency with the 1) the Kestrel Meridian Logo (www.kestrelmeridian.org), 2) the visual identity from the fist event and 3) the organization TLQ Logo (www.t7lq.org) -- but the design should be modern, clean, and crisp.

Target Market(s)

Corporations, academics, executives, entrepreneurs, consultants, multilateral organizations, founders, institutions

Industry/Entity Type

Business

Coding

Coded - Design and coding required

Number of Pages Required

5+ page

Font styles to use
Sans Serif

Colors
f68d4d
9bcb3b
3276b5
faa54b
00a88f
0792cd
f37022
9bcb3c
0355a3

Requirements
Must have
• maintain consistency with Kestrel Meridian Logo
• dynamic to get the attention
• design modern, clean and crisp
• content should be well linked (e.i. photos and bios liked to the name of speaker on sessions).
• Has to link to a registration system
• Needs to be under the Kestrel Meridian domain www.kestrelmeridian.org
• Preference to URL kestrelmeridian.org/Summit2015
Nice to have
• different techniques to display menus, photos and bios and description of sessions
• connect somehow with the visual communication developed on last summit in 2013
Should not have
• should not be the same previously
• should not be traditional
• should not be static

```html
<!DOCTYPE html>
<html lang="en">
<head>
<meta charset="utf-8">
<title>Program Details – Kestrel Meridian Forum 2015</title>
<link rel="stylesheet" href="https://fonts.googleapis.com/css2?family=Open+Sans:wght@400;600;700&display=swap">
<style>
:root{
  --navy:#0b3d82;
  --blue:#0355a3;
  --title:#1c4f9c;
  --orange:#f37022;
  --green:#8db84a;
  --green-btn:#7cc039;
  --text:#666;
  --muted:#888;
  --band:#e9e9e9;
  --footer:#ececec;
  --line:#d8d8d8;
}
*{box-sizing:border-box;margin:0;padding:0}
html,body{width:918px;height:1200px;overflow:hidden;background:#fff}
body{font-family:"Open Sans",Arial,sans-serif;color:var(--text);position:relative}
.abs{position:absolute}
.top-rule{left:0;top:0;width:918px;height:5px;background:var(--navy)}
.brand{left:76px;top:40px;display:flex;align-items:center;gap:8px}
.brand-mark{width:34px;height:34px;border-radius:50%;background:var(--blue)}
.brand-name{font-size:17px;font-weight:600;color:var(--navy);line-height:1.05;width:120px}
.event-date{right:406px;top:18px;text-align:right;line-height:1.15}
.event-date .day{font-size:16px;color:var(--navy);display:block}
.event-date .place{font-size:13px;color:var(--orange)}
.countdown{left:533px;top:22px;width:181px;height:29px;border:1px solid var(--line);border-radius:2px;display:flex;align-items:center;justify-content:space-around;padding:0 3px}
.countdown .unit{display:flex;align-items:center;gap:2px}
.countdown .lbl{font-size:4px;writing-mode:vertical-rl;transform:rotate(180deg);color:#555}
.countdown .num{font-size:12px;font-weight:700;color:#222;background:#f1f1f1;border:1px solid #999;padding:0 2px;letter-spacing:1px;line-height:16px}
.register{left:732px;top:23px;width:110px;height:28px;background:var(--green-btn);color:#fff;font-size:11px;display:flex;align-items:center;justify-content:center;gap:6px;border-radius:1px}
.skyline{left:588px;top:74px;width:250px;height:39px;background:linear-gradient(90deg,#f3f3f3,#e4e4e4)}
.nav{left:228px;top:113px;width:614px;height:33px;background:var(--navy);display:flex;align-items:center}
.nav a{color:#fff;text-decoration:none;font-size:9.6px;font-weight:600;height:100%;display:flex;align-items:center;padding:0 10.5px;text-transform:uppercase}
.nav a.active{background:var(--green);padding:0 11px}
.crumbs{left:0;top:146px;width:918px;height:29px;background:var(--band);font-size:8.5px;color:#555;display:flex;align-items:center;padding-left:76px;gap:10px}
.crumbs .home{color:var(--blue)}
.crumbs .sep{color:var(--blue);font-size:8px}
.page-title{left:76px;top:202px;font-size:22px;font-weight:600;color:var(--title)}
.article{left:77px;top:246px;width:762px;height:572px;border:1px solid var(--line)}
.hero{left:3px;top:3px;width:321px;height:204px;background:radial-gradient(circle at 35% 25%,#e9845a 0,#b9523e 25%,#5b3c4f 55%,#2e3350 100%)}
.lead{left:340px;top:16px;width:400px}
.lead h2{font-size:16.5px;font-weight:400;color:#222;line-height:1.2}
.lead time{display:block;font-size:8px;color:#333;margin:3px 0 14px}
p{font-size:8.6px;line-height:14.4px;margin-bottom:7px}
.body-copy{left:19px;top:229px;width:726px}
.body-copy p{margin-bottom:14.4px}
.share{left:19px;top:508px;display:flex;gap:6px}
.share span{width:20px;height:20px;border-radius:2px;background:#c9d1de;border:1px solid #9aa6ba}
.share .mail{background:#f4f4f4;border-color:#bbb;display:flex;align-items:center;justify-content:center}
.sponsors{left:83px;top:855px;width:375px}
.partners{left:476px;top:855px;width:370px}
.group-label{font-size:9.5px;color:#777}
.logo-row{display:flex;align-items:center;gap:12px;margin-top:18px;height:44px}
.logo-row span{font-size:10.5px;font-weight:600;color:var(--navy);white-space:nowrap}
.divider{left:458px;top:857px;width:1px;height:68px;background:var(--line)}
.footer{left:0;top:970px;width:918px;height:171px;background:var(--footer)}
.fcol h3{font-size:10px;font-weight:600;color:var(--navy);text-transform:uppercase;margin-bottom:14px}
.org{display:flex;align-items:center;gap:6px;margin-bottom:16px}
.org i{width:26px;height:26px;border-radius:50%;background:var(--orange);display:block}
.org.uni i{border-radius:0;background:#1f5e3a}
.org span{font-size:10px;font-weight:600;color:#444;line-height:1.15;width:90px}
.vline{width:1px;height:110px;background:#d2d2d2;top:998px}
.contact{font-size:8.4px;color:#888;line-height:13px}
.contact .row{display:flex;gap:7px;margin-bottom:8px}
.contact svg{flex:none;margin-top:2px}
.quick a{display:block;font-size:6.6px;font-weight:600;color:#777;text-decoration:none;text-transform:uppercase;line-height:13px}
.news input{width:120px;height:20px;border:1px solid #ddd;font:8px "Open Sans",sans-serif;padding-left:7px;color:#666}
.news button{width:27px;height:20px;border:0;background:#c8c8c8;position:absolute;left:93px;top:0}
.follow{display:flex;gap:7px;margin-top:6px}
.follow span{width:20px;height:20px;border-radius:50%;background:var(--navy)}
.follow span:nth-child(2){background:#2aa3e0}
.follow span:nth-child(3){background:#0b6aa8}
.follow span:nth-child(4){background:#f58a2a}
.bottom{left:0;top:1141px;width:918px;height:59px;background:var(--blue);color:#fff;font-size:8.6px;display:flex;align-items:center;padding-left:76px}
.to-top{left:822px;top:1160px;width:19px;height:19px;border:1.5px solid #9ec0e6;border-radius:50%;display:flex;align-items:center;justify-content:center}
</style>
</head>
<body>
<div class="abs top-rule"></div>

<header>
  <a class="abs brand" aria-label="Kestrel Meridian home">
    <span class="brand-mark"></span>
    <span class="brand-name">Kestrel Meridian</span>
  </a>
  <div class="abs event-date"><span class="day">July 16 and 17, 2015</span><span class="place">Harrowgate, Vermont</span></div>
  <div class="abs countdown">
    <div class="unit"><span class="lbl">weeks</span><span class="num">01</span></div>
    <div class="unit"><span class="lbl">days</span><span class="num">06</span></div>
    <div class="unit"><span class="lbl">hours</span><span class="num">21</span></div>
    <div class="unit"><span class="lbl">mins</span><span class="num">02</span></div>
    <div class="unit"><span class="lbl">secs</span><span class="num">30</span></div>
  </div>
  <a class="abs register">
    <svg width="11" height="11" viewBox="0 0 12 12"><rect x="1" y="2" width="8" height="9" fill="none" stroke="#fff" stroke-width="1.4"/><path d="M5 7l6-6" stroke="#fff" stroke-width="1.6"/></svg>
    Register Now
  </a>
  <div class="abs skyline" role="img" aria-label="Light grey line drawing of growth chart, farm, water, city and transport"></div>
  <nav class="abs nav">
    <a class="active">Home</a>
    <a>Kestrel Meridian</a>
    <a>Knowledge Base</a>
    <a>Sponsors &amp; Partners</a>
    <a>Join Us</a>
    <a>Events</a>
    <a>Contactus</a>
  </nav>
</header>

<div class="abs crumbs"><span class="home">Home</span><span class="sep">››</span><span>Agenda</span><span class="sep">››</span><span>Program Details</span></div>

<h1 class="abs page-title">Program Details</h1>

<article class="abs article">
  <div class="abs hero" role="img" aria-label="Speaker at a podium addressing a large conference audience"></div>
  <div class="abs lead">
    <h2>Praesent iaculis faucibus urna sit amet lacinia</h2>
    <time>Feb 23, 2015</time>
    <p>Fusce nec leo ac urna pulvinar auctor. Mauris bibendum fringilla velit. Nulla in lorem at massa pellentesque posuere. Nulla tristique posuere molestie. Aliquam erat volutpat. Etiam quis aliquet risus. Duis ornare erat eget magna dapibus, in accumsan quam pharetra. Nam tempus, quam in bibendum vulputate, sapien dolor viverra nisl, vitae euismod elit turpis et nulla. Aliquam erat volutpat. Pellentesque blandit lacus eget nunc faucibus, et tincidunt eros viverra. Maecenas consequat justo enim, ac mattis massa imperdiet quis.</p>
    <p>Fusce sollicitudin lorem et luctus volutpat. Proin placerat dapibus gravida. In tristique tristique nulla eget hendrerit. Maecenas vel tortor accumsan quam varius imperdiet vel eget elit. Aenean facilisis tincidunt lectus, id dictum nisi luctus eget. Vivamus efficitur ex condimentum, malesuada eros eget, feugiat nibh.</p>
  </div>
  <div class="abs body-copy">
    <p>Aliquam erat volutpat. Quisque aliquet ex nec est vestibulum pulvinar. Pellentesque convallis molestie enim sit amet efficitur. Etiam id imperdiet lectus. Vivamus lacus justo, ultrices nec erat in, euismod iaculis mauris. Vivamus eleifend vitae nulla vel malesuada. In ac malesuada lacus, et consectetur ante. Fusce vitae lectus sit amet mi pulvinar maximus. Aenean placerat, nibh vel accumsan aliquet, magna nibh accumsan nibh, ac tempus nunc ipsum ac tellus. Cras augue magna, placerat eget nulla non, congue suscipit neque.</p>
    <p>Proin a dolor mauris. Vestibulum ante ipsum primis in faucibus orci luctus et ultrices posuere cubilia Curae; Vestibulum eget nisl metus. Phasellus nisl est, condimentum vitae faucibus in, sollicitudin vel metus. Nunc sit amet consequat risus. Curabitur ac elit leo. In eleifend dui tellus, in scelerisque elit porttitor et. Integer eu massa lacinia, lacinia nulla non, volutpat purus. Sed libero felis, vestibulum et dolor eget, lacinia aliquet neque.</p>
    <p>Aenean sed quam non sapien faucibus consequat vitae sit amet orci. Praesent quis risus mi. In mollis nulla in pulvinar dictum. Vivamus interdum sagittis felis, ut dapibus ligula feugiat ac. In dictum sapien eu tellus finibus fermentum. Aenean faucibus lacus ut mollis commodo. Donec vestibulum odio sem, ac laoreet massa ullamcorper id. Donec molestie nisi et tellus hendrerit vehicula. Nunc eu ligula sed quam pulvinar maximus in vitae eros. Proin porta fermentum ipsum, vel porttitor turpis venenatis luctus. Vivamus volutpat eu sapien quis tempus. Aenean feugiat viverra lorem ac sagittis. Donec sit amet lectus nec mi tempor laoreet ac nec nunc. Duis id auctor sapien.</p>
    <p>Nullam accumsan purus vel tempus viverra. Mauris suscipit felis id nunc elementum varius. Praesent elementum nulla sit amet justo pellentesque scelerisque. Nam et tortor in ante iaculis porttitor in luctus mi. Vivamus gravida sem a pretium euismod. Nam lobortis, purus et fringilla tempus, risus eros dignissim diam, eget finibus sem risus sit amet eros. Vestibulum facilisis dolor at purus tincidunt porta. Nam fringilla nulla vel nisl condimentum, dapibus condimentum enim porta. Phasellus blandit quam a ipsum gravida dapibus. Cras sed augue tortor. Suspendisse elit ligula, iaculis dignissim justo eu, vestibulum venenatis elit. Sed egestas, nisl id cursus ultricies, turpis orci rhoncus odio, id tristique odio ex in lacus. Nam suscipit sapien eget blandit sollicitudin.</p>
  </div>
  <div class="abs share" aria-label="Share">
    <span aria-label="Share on social network one"></span>
    <span aria-label="Share on social network two"></span>
    <span aria-label="Share on social network three"></span>
    <span class="mail" aria-label="Share by email"><svg width="14" height="10" viewBox="0 0 14 10"><rect x=".5" y=".5" width="13" height="9" fill="none" stroke="#999"/><path d="M.5 .5L7 6l6.5-5.5" fill="none" stroke="#999"/></svg></span>
  </div>
</article>

<section class="abs sponsors">
  <div class="group-label">Diamond Sponsors</div>
  <div class="logo-row"><span>Corvane Alloys</span><span>Brightwell Foods</span><span>Stonemark</span><span>Aldermoor Health</span></div>
</section>
<div class="abs divider"></div>
<section class="abs partners">
  <div class="group-label">Partners and Collaborators</div>
  <div class="logo-row"><span>Ferris Lowell Institute</span><span>Halvard Center</span><span>Rootline Promise</span><span>Open Harvest Lab</span></div>
</section>

<footer>
  <div class="abs footer"></div>
  <div class="abs fcol" style="left:76px;top:997px">
    <h3>Organizers</h3>
    <div class="org"><i></i><span>TLQ Trust for Lasting Quality</span></div>
    <div class="org uni"><i></i><span>Northfield State University</span></div>
  </div>
  <div class="abs vline" style="left:210px"></div>
  <div class="abs fcol" style="left:239px;top:997px;width:340px">
    <h3>Contact Us</h3>
    <div class="contact" style="display:flex;gap:40px">
      <div>
        <div class="row"><svg width="6" height="9" viewBox="0 0 6 9"><path d="M3 9L.5 4A2.5 2.5 0 1 1 5.5 4z" fill="#aaa"/></svg><span>Conference Content Questions<br>55 Building name, Street name<br>City - Zipcode</span></div>
        <div class="row"><svg width="8" height="8" viewBox="0 0 8 8"><path d="M1 1l2 0 1 2-1 1a5 5 0 0 0 2 2l1-1 2 1v2C4 8 0 4 1 1z" fill="#aaa"/></svg><span>Phone: (555) 014-2287</span></div>
        <div class="row"><svg width="9" height="7" viewBox="0 0 9 7"><rect width="9" height="7" fill="#aaa"/><path d="M0 0l4.5 4L9 0" fill="none" stroke="#ececec"/></svg><span>lena.morrow@t7lq.org</span></div>
      </div>
      <div>
        <div class="row"><svg width="6" height="9" viewBox="0 0 6 9"><path d="M3 9L.5 4A2.5 2.5 0 1 1 5.5 4z" fill="#aaa"/></svg><span>Registration Questions<br>55 Building name, Street name<br>City - Zipcode</span></div>
        <div class="row"><svg width="8" height="8" viewBox="0 0 8 8"><path d="M1 1l2 0 1 2-1 1a5 5 0 0 0 2 2l1-1 2 1v2C4 8 0 4 1 1z" fill="#aaa"/></svg><span>Phone: (555) 019-4410</span></div>
        <div class="row"><svg width="9" height="7" viewBox="0 0 9 7"><rect width="9" height="7" fill="#aaa"/><path d="M0 0l4.5 4L9 0" fill="none" stroke="#ececec"/></svg><span>registration@northfieldstate.edu</span></div>
      </div>
    </div>
  </div>
  <div class="abs vline" style="left:585px"></div>
  <div class="abs fcol quick" style="left:602px;top:997px">
    <h3>Quick Links</h3>
    <a>• Home</a><a>• Kestrel Meridian</a><a>• Knowledge Base</a><a>• Sponsors &amp; Partners</a><a>• Join Us</a><a>• Events</a><a>• Contactus</a>
  </div>
  <div class="abs vline" style="left:702px"></div>
  <div class="abs fcol news" style="left:722px;top:997px">
    <h3>Newsletter</h3>
    <div style="position:relative;height:20px;margin:-4px 0 20px -1px">
      <input type="text" placeholder="E-mail">
      <button aria-label="Subscribe"><svg width="9" height="10" viewBox="0 0 9 10"><path d="M0 0l9 5-9 5z" fill="#888"/></svg></button>
    </div>
    <h3 style="margin-bottom:4px">Follow Us On</h3>
    <div class="follow"><span></span><span></span><span></span><span></span></div>
  </div>
  <div class="abs bottom">Copyright &nbsp;©&nbsp; 2015 &nbsp;Kestrel Meridian Summit 2015. &nbsp; All rights reserved.</div>
  <a class="abs to-top" aria-label="Back to top"><svg width="9" height="7" viewBox="0 0 9 7"><path d="M4.5 0L9 7H0z" fill="#9ec0e6"/></svg></a>
</footer>
</body>
</html>
```